Dr Oliver Kimpton needs a logo for letter head and business cards

I need a logo design for my stationery (letter head & business card). I am a Respiratory and Sleep medicine doctor who treats adults.
I treat asthma, snoring and other breathing problems and the symbols could include something relating to this. examples: ZZZ or a bed etc for snoring/sleep, a symbol of lungs , or other option. The blue lung could include a small red circle in the left one to indicate lung cancer.

Ideally in blue or green colour with maybe a small amount of red to indicate illness in the lung or somehow related to sleep.

the second side of the business card could include the text below:

Your next appointment is:
On ________________at_______________AM/PM

Please call to reschedule if necessary.

Target Market(s)

Middle aged to elderly patients and other medical staff. Professional context.

Industry/Entity Type

Medical

Contact Information for Business Card

Dr Oliver Kimpton
MBBS (hons),
FRACP (Sleep & Respiratory).
DTM&H, MHSM, GC-CU.
www.orindalemedgroup.example

Locations:
Tallowmere Private Specialist Consulting Rooms,
Level1, 618 Tullock Lane,
Harlowdene Vic 3961
Ph: 9471 3620
Fax: 8316 5094

Logo Text

that this is a respectable and trustworthy medical specialist

Font styles to use
Sans Serif

Colors
34a6d7
0655a3
33b8a4
00a88f
85cae6
ec1f27

Requirements
Must have
• my name in the logo . I have included my current business card and need to replace the logo/wording in the top right corner "Tallowmere Private specialist Consulting Rooms" for my own personalised logo.
Nice to have
• symbol relating to lungs /breathing and sleep
Should not have
• Should not have the location in the logo of the business card

```html
<!DOCTYPE html>
<html lang="en">
<head>
<meta charset="utf-8">
<title>Dr Oliver Kimpton – Stationery</title>
<link href="https://fonts.googleapis.com/css2?family=Roboto+Condensed:ital,wght@0,400;0,700;1,400&display=swap" rel="stylesheet">
<style>
  :root{
    --blue:#0a8fdc;
    --teal:#43b093;
    --ink:#1a1a1a;
    --white:#ffffff;
    --stage:#c0c0c0;
  }
  *{box-sizing:border-box;margin:0;padding:0}
  html,body{width:1200px;height:1200px;overflow:hidden;background:var(--white)}
  body{position:relative;font-family:"Roboto Condensed",sans-serif}
  .showcase{position:absolute;left:0;top:0;width:1200px;height:598px;background:var(--white)}
  .wordmark{position:absolute;color:var(--blue);font-weight:400;line-height:1;letter-spacing:.02em;text-transform:uppercase;white-space:nowrap}
  .wordmark span{display:block}
  .wordmark--hero{left:0;width:1200px;top:198px;text-align:center}
  .wordmark--hero .line-1{font-size:116px}
  .wordmark--hero .line-2{font-size:88px;margin-top:2px}
  .stage{position:absolute;left:0;top:598px;width:1200px;height:602px;background:var(--stage)}
  .card{position:absolute;top:832px;width:476px;height:279px;background:var(--white);overflow:hidden}
  .card--front{left:101px}
  .card--back{left:606px}
  .card--front .wordmark{left:30px;top:34px}
  .card--front .wordmark .line-1{font-size:38px}
  .card--front .wordmark .line-2{font-size:32px}
  .card--back .wordmark{right:22px;top:16px;text-align:right}
  .card--back .wordmark .line-1{font-size:29px}
  .card--back .wordmark .line-2{font-size:25px}
  .lung-panel{position:absolute;top:22px;height:250px;width:139px;background:var(--teal)}
  .card--front .lung-panel{left:337px;border-radius:80px 6px 10px 26px}
  .card--back .lung-panel{left:0;border-radius:6px 80px 26px 10px}
  .holder{position:absolute;left:38px;top:186px;color:var(--teal);font-size:21px}
  .credentials{position:absolute;left:38px;top:214px;color:var(--ink);font-size:12px;line-height:1.35}
  .address{position:absolute;right:28px;top:178px;color:var(--white);font-size:13px;line-height:1.18;text-align:right}
  .appt-title{position:absolute;left:22px;top:130px;color:var(--white);font-weight:700;font-size:15px;line-height:1;letter-spacing:.03em}
  .web{position:absolute;left:88px;top:16px;color:var(--teal);font-style:italic;font-size:13px}
  .slots{position:absolute;left:186px;top:73px;width:268px;list-style:none}
  .slot{display:flex;align-items:flex-end;height:39.5px;color:var(--teal);font-size:14px;line-height:1}
  .slot .blank{border-bottom:1px solid var(--teal);height:13px}
  .slot .b1{width:91px}
  .slot .b2{width:102px}
  .note{position:absolute;right:24px;top:247px;color:var(--teal);font-size:12px}
</style>
</head>
<body>
  <section class="showcase">
    <div class="wordmark wordmark--hero"><span class="line-1">Dr Oliver</span><span class="line-2">Kimpton</span></div>
  </section>

  <section class="stage"></section>

  <article class="card card--front">
    <div class="wordmark"><span class="line-1">Dr Oliver</span><span class="line-2">Kimpton</span></div>
    <div class="lung-panel" role="img" aria-label="Teal lung silhouette with windpipe"></div>
    <p class="address">618 Tullock Lane<br>Harlowdene Vic 3961<br>Tel: 9471 3620<br>Fax: 8316 5094</p>
    <p class="holder">Dr Oliver Kimpton</p>
    <p class="credentials">MBBS(Hon),<br>FRACP(Thoracic Medicine),<br>MPH</p>
  </article>

  <article class="card card--back">
    <div class="lung-panel" role="img" aria-label="Teal lung silhouette with windpipe"></div>
    <p class="appt-title">YOUR<br>NEXT<br>APPOINTMENT<br>IS:</p>
    <p class="web">www.tallowmereprivate.example</p>
    <div class="wordmark"><span class="line-1">Dr Oliver</span><span class="line-2">Kimpton</span></div>
    <ul class="slots">
      <li class="slot">On<span class="blank b1"></span>at<span class="blank b2"></span>AM/PM</li>
      <li class="slot">On<span class="blank b1"></span>at<span class="blank b2"></span>AM/PM</li>
      <li class="slot">On<span class="blank b1"></span>at<span class="blank b2"></span>AM/PM</li>
      <li class="slot">On<span class="blank b1"></span>at<span class="blank b2"></span>AM/PM</li>
    </ul>
    <p class="note">Please call to reschedule if necessary</p>
  </article>
</body>
</html>
```